Wattlebloom Berry Farm

I would like the our logo
a mixture of berries
and a kookaburra
Mark & Helen Dorsendi
Farm Fresh & Frozen Strawberries Raspberries & other berries
Homemade award winning Jams, Syrups & Vinegars
ph: 0493517604
Email: helmar@quorvanet.com.au
web www.wattlebloom.com.au
48 Fenwick Road Brambledale Vic 3781
BUY DIRECT FROM FARM

Farm

```html
<!DOCTYPE html>
<html lang="en">
<head>
<meta charset="utf-8">
<title>Wattlebloom Berry Farm – Business Card</title>
<link rel="stylesheet" href="https://fonts.googleapis.com/css2?family=Andika:wght@400;700&display=swap">
<style>
  :root {
    --farm-green: #3a8d4d;
    --ink: #1f1f1f;
    --card-white: #ffffff;
    --card-edge: #c9c9c9;
    --backdrop-light: #fafafa;
    --backdrop-dark: #e3e4e4;
  }
  * { margin: 0; padding: 0; box-sizing: border-box; }
  html, body { width: 1200px; height: 900px; overflow: hidden; }
  body {
    background: radial-gradient(ellipse at center, var(--backdrop-light) 40%, var(--backdrop-dark) 100%);
    font-family: "Andika", sans-serif;
    position: relative;
  }
  .card {
    position: absolute;
    left: 68px; top: 125px;
    width: 1064px; height: 650px;
    background: var(--card-white);
    border: 1px solid var(--card-edge);
  }
  .side-band {
    position: absolute;
    left: 0; top: 0;
    width: 148px; height: 100%;
    background: var(--farm-green);
  }
  .brand-seal {
    position: absolute;
    left: 37px; top: 414px;
    width: 210px; height: 210px;
    border-radius: 50%;
    background: var(--card-white);
    display: flex; align-items: center; justify-content: center;
    text-align: center;
  }
  .brand-name {
    color: var(--farm-green);
    font-weight: 700;
    font-size: 25px;
    line-height: 1.15;
    width: 170px;
  }
  .contact {
    position: absolute;
    left: 284px; top: 454px;
    color: var(--ink);
  }
  .contact-names {
    color: var(--farm-green);
    font-weight: 700;
    font-size: 22px;
    line-height: 30px;
    letter-spacing: 0.6px;
    margin-bottom: 1px;
  }
  .contact-line {
    font-size: 21.5px;
    line-height: 32px;
    white-space: nowrap;
  }
  .divider {
    position: absolute;
    left: 284px; top: 553px;
    width: 751px; height: 2px;
    background: var(--ink);
  }
  .offerings {
    position: absolute;
    left: 284px; top: 570px;
    font-size: 18.5px;
    line-height: 26px;
    text-transform: uppercase;
    color: var(--ink);
    white-space: nowrap;
  }
</style>
</head>
<body>
  <main class="card">
    <div class="side-band"></div>
    <div class="brand-seal">
      <span class="brand-name">Wattlebloom Berry Farm</span>
    </div>
    <section class="contact">
      <h1 class="contact-names">MARK &amp; HELEN DORSENDI</h1>
      <p class="contact-line">ph: 0493517604, Email: helmar@quorvanet.com.au</p>
      <p class="contact-line">web www.wattlebloom.com.au, 48 Fenwick Road Brambledale Vic 3781</p>
    </section>
    <div class="divider"></div>
    <p class="offerings">Farm fresh &amp; frozen strawberries raspberries &amp; other berries<br>Homemade award winning jams, syrups &amp; vinegars</p>
  </main>
</body>
</html>
```